"Harbor Constructors" is a residential building company and needs a new business card design and may re

We would like a redesign based on the existing logo, and would like to see a new font as well. We are bespoke home builders who build sustainable energy efficient homes.

Industry/Entity Type

Construction

Contact Information for Business Card

Business card size 40mm x 90mm

Colors

Designer to choose colors to be used in the design.

```html
<!DOCTYPE html>
<html lang="en">
<head>
<meta charset="utf-8">
<title>Harbor Constructors – Business Card</title>
<link rel="stylesheet" href="https://fonts.googleapis.com/css2?family=Arimo:wght@400;700&display=swap">
<style>
  :root {
    --card-navy: #1e2433;
    --copper: #c6a48a;
    --backdrop: #ece8e3;
  }
  * { margin: 0; padding: 0; box-sizing: border-box; }
  html, body {
    width: 1200px;
    height: 800px;
    overflow: hidden;
    background: var(--backdrop);
    font-family: "Arimo", Arial, sans-serif;
  }
  .canvas {
    position: relative;
    width: 1200px;
    height: 800px;
    display: flex;
    align-items: center;
    justify-content: center;
    gap: 60px;
  }
  .card {
    position: relative;
    width: 520px;
    height: 300px;
    background: var(--card-navy);
    color: var(--copper);
    box-shadow: 0 6px 18px rgba(0,0,0,0.18);
  }
  .card-front {
    display: flex;
    align-items: center;
    justify-content: center;
    gap: 14px;
  }
  .brand-mark {
    width: 22px;
    height: 22px;
    background: var(--copper);
  }
  .brand-name {
    font-size: 34px;
    font-weight: 400;
    letter-spacing: 0.5px;
  }
  .card-back .holder-name {
    position: absolute;
    left: 52px;
    top: 40px;
    font-size: 30px;
    font-weight: 700;
    line-height: 1.2;
    letter-spacing: 0.3px;
  }
  .contact-list {
    position: absolute;
    left: 200px;
    top: 150px;
    list-style: none;
    font-size: 15px;
    line-height: 22px;
  }
  .contact-list .reg-line {
    display: flex;
    gap: 36px;
  }
</style>
</head>
<body>
  <main class="canvas">
    <section class="card card-front" aria-label="Card front">
      <span class="brand-mark" aria-hidden="true"></span>
      <span class="brand-name">Harbor Constructors</span>
    </section>

    <section class="card card-back" aria-label="Card back">
      <h1 class="holder-name">Daniel<br>Moretti</h1>
      <ul class="contact-list">
        <li>0400 555 018</li>
        <li>daniel@harborconstructors.com.au</li>
        <li>www.harborconstructors.com.au</li>
        <li>PO Box 4120 Northgate LPO Easton WA 6999</li>
        <li class="reg-line"><span>Registration 40782</span><span>ABN: 12 345 678 901</span></li>
      </ul>
    </section>
  </main>
</body>
</html>
```